Business card design needed

A laid back coffee shop that has a great feel, that becomes a bar and grill at night. We are also wanting to cater for functions etc.
The business itself is painted dark blue/charcoal and has red doors.
Would like a logo that will be recognised when seen.

Industry/Entity Type

Coffee Shop

Contact Information for Business Card

The Lantern Coffee Bar & Grill
14b Wattle Rd
Kelmora NSW 2318
Ph. 02 4817 3362

Logo Text

Logo styles of interest
Emblem Logo
Abstract Logo
Wordmark Logo
Requirements
Must have
• A loyalty card on the back with 2 rows of 7 stamp spaces and a place to write a name and phone number (for a draw)

```html
<!DOCTYPE html>
<html lang="en">
<head>
<meta charset="utf-8">
<title>The Lantern Coffee Bar &amp; Grill — Business &amp; Loyalty Card</title>
<link rel="stylesheet" href="https://fonts.googleapis.com/css2?family=Montserrat:wght@300;700&display=swap">
<style>
  :root {
    --page: #ffffff;
    --ocean-light: #1ea6df;
    --ocean-dark: #0a6aa3;
    --band: rgba(255, 255, 255, 0.14);
    --charcoal-light: #4a4a4c;
    --charcoal-dark: #1f1f21;
    --signal-red: #e0222b;
    --ring-blue: #23a0dc;
    --white: #ffffff;
    --stamp: #cfcfd2;
  }
  * { box-sizing: border-box; margin: 0; padding: 0; }
  html, body {
    width: 1200px;
    height: 709px;
    overflow: hidden;
    background: var(--page);
    font-family: "Montserrat", Arial, sans-serif;
  }
  .canvas { position: relative; width: 1200px; height: 709px; }

  .card { position: absolute; box-shadow: 0 10px 18px rgba(0, 0, 0, 0.22); }

  /* Front: business card */
  .card-front {
    left: 24px; top: 109px; width: 661px; height: 387px;
    background: radial-gradient(ellipse 60% 75% at 50% 38%, var(--ocean-light), var(--ocean-dark));
  }
  .brand {
    position: absolute; left: 0; right: 0;
    display: flex; flex-direction: column; align-items: center;
  }
  .card-front .brand { top: 28px; }
  .brand-mark { border-radius: 50%; background: var(--signal-red); }
  .card-front .brand-mark { width: 190px; height: 190px; }
  .brand-name {
    color: var(--white); font-weight: 700; text-align: center;
    text-transform: uppercase; line-height: 1.15;
  }
  .card-front .brand-name { margin-top: 14px; font-size: 32px; letter-spacing: 1px; }
  .brand-name .tagline { display: block; font-size: 0.64em; letter-spacing: 0.5px; }

  .address-band {
    position: absolute; left: 0; right: 0; top: 349px; height: 38px;
    background: var(--band);
    display: flex; align-items: center; justify-content: center;
    color: var(--white); font-weight: 300; font-size: 18.5px;
  }

  /* Back: loyalty card */
  .card-back {
    left: 778px; top: 13px; width: 382px; height: 661px;
    background: radial-gradient(ellipse 80% 60% at 50% 20%, var(--charcoal-light), var(--charcoal-dark));
  }
  .card-back .brand { top: 32px; }
  .card-back .brand-mark {
    width: 168px; height: 168px;
    box-shadow: 0 0 0 7px var(--ring-blue);
  }
  .card-back .brand-name { margin-top: 16px; font-size: 26px; }

  .stamp-grid {
    position: absolute; left: 16px; top: 292px;
    display: grid; grid-template-columns: 170px 170px; column-gap: 11px; row-gap: 11px;
  }
  .stamp-slot { height: 25px; border-radius: 12.5px; background: var(--stamp); }

  .entry-fields {
    position: absolute; left: 16px; right: 16px; top: 552px;
    display: flex; flex-direction: column; gap: 18px;
  }
  .entry-line {
    display: flex; align-items: flex-end; gap: 10px;
    color: var(--white); font-weight: 700; font-size: 14px;
    text-transform: uppercase; letter-spacing: 0.5px;
  }
  .entry-line .write-space {
    flex: 1; height: 1px; margin-bottom: 3px;
    border-bottom: 2px solid var(--stamp);
  }
</style>
</head>
<body>
<main class="canvas">
  <section class="card card-front" aria-label="Business card front">
    <div class="brand">
      <div class="brand-mark" aria-hidden="true"></div>
      <p class="brand-name">The Lantern<span class="tagline">Coffee Bar &amp; Grill</span></p>
    </div>
    <p class="address-band">14b Wattle Rd Kelmora NSW 2318 Ph. 02 4817 3362</p>
  </section>

  <section class="card card-back" aria-label="Loyalty card back">
    <div class="brand">
      <div class="brand-mark" aria-hidden="true"></div>
      <p class="brand-name">The Lantern<span class="tagline">Coffee Bar &amp; Grill</span></p>
    </div>
    <div class="stamp-grid" aria-label="Loyalty stamp spaces">
      <div class="stamp-slot"></div><div class="stamp-slot"></div>
      <div class="stamp-slot"></div><div class="stamp-slot"></div>
      <div class="stamp-slot"></div><div class="stamp-slot"></div>
      <div class="stamp-slot"></div><div class="stamp-slot"></div>
      <div class="stamp-slot"></div><div class="stamp-slot"></div>
      <div class="stamp-slot"></div><div class="stamp-slot"></div>
      <div class="stamp-slot"></div><div class="stamp-slot"></div>
    </div>
    <div class="entry-fields" aria-label="Prize draw details">
      <p class="entry-line">Name <span class="write-space"></span></p>
      <p class="entry-line">Phone <span class="write-space"></span></p>
    </div>
  </section>
</main>
</body>
</html>
```